Corporate Business Card

Very professional, Modern, Not to busy, include phone address email, website
(555) 317-4860, 18716 52nd Avenue S, Marlow Falls, OR 98417, marcus@bralvintrust.example, vendrikworks.example

Target Market(s)

Manufacturing

Industry/Entity Type

Aero, machining, manufacturing, Off road racing

Contact Information for Business Card

Phone, address email, website

```html
<!DOCTYPE html>
<html lang="en">
<head>
<meta charset="utf-8">
<title>Vendrik Works — Business Card</title>
<link rel="stylesheet" href="https://fonts.googleapis.com/css2?family=Montserrat:wght@300;400;500;700;800&display=swap">
<style>
  :root {
    --navy: #06286d;
    --navy-deep: #03235f;
    --red: #e0141e;
    --white: #ffffff;
    --ink-grey: #555a63;
    --backdrop: #858585;
  }
  html, body {
    margin: 0;
    padding: 0;
    width: 1200px;
    height: 1056px;
    overflow: hidden;
    background: var(--backdrop);
    font-family: "Montserrat", sans-serif;
  }
  .sheet {
    position: relative;
    width: 1200px;
    height: 1056px;
  }
  .card {
    position: absolute;
    left: 190px;
    width: 820px;
    height: 468px;
    box-sizing: border-box;
    box-shadow: 0 10px 28px rgba(0,0,0,0.25);
  }
  .card--front { top: 40px; background: var(--white); }
  .card--back  { top: 548px; background: var(--navy-deep); }

  /* Front */
  .brand {
    position: absolute;
    left: 56px;
    top: 52px;
  }
  .brand__name {
    font-weight: 800;
    font-size: 44px;
    letter-spacing: 1px;
    color: var(--navy);
    line-height: 1;
  }
  .brand__rule {
    width: 150px;
    height: 2px;
    background: var(--navy);
    margin-top: 14px;
  }
  .person {
    position: absolute;
    right: 60px;
    top: 170px;
    text-align: right;
  }
  .person__name {
    font-size: 34px;
    line-height: 1.1;
    letter-spacing: 1px;
    text-transform: uppercase;
  }
  .person__first { font-weight: 300; color: var(--navy); }
  .person__last  { font-weight: 700; color: var(--red); }
  .person__title {
    font-size: 22px;
    font-weight: 400;
    color: var(--ink-grey);
    margin-top: 6px;
    letter-spacing: 1px;
  }
  .contact {
    position: absolute;
    left: 56px;
    top: 270px;
    font-size: 19px;
    color: var(--ink-grey);
    line-height: 1.55;
  }
  .contact__row {
    display: flex;
    align-items: center;
    gap: 10px;
  }
  .contact__icon { width: 16px; height: 16px; flex: none; }
  .contact__address { margin-top: 10px; }

  /* Back */
  .back-brand {
    position: absolute;
    left: 0;
    right: 0;
    top: 190px;
    text-align: center;
  }
  .back-brand__name {
    font-weight: 800;
    font-size: 56px;
    letter-spacing: 2px;
    color: var(--white);
    line-height: 1;
  }
  .back-brand__rule {
    width: 220px;
    height: 2px;
    background: var(--white);
    margin: 22px auto 0;
  }
</style>
</head>
<body>
<main class="sheet">
  <section class="card card--front" aria-label="Business card front">
    <div class="brand">
      <div class="brand__name">Vendrik Works</div>
      <div class="brand__rule"></div>
    </div>

    <div class="person">
      <div class="person__name"><span class="person__first">Marcus</span> <span class="person__last">Halden</span></div>
      <div class="person__title">Director / CEO</div>
    </div>

    <div class="contact">
      <div class="contact__row">
        <svg class="contact__icon" viewBox="0 0 24 24" aria-hidden="true"><path fill="#06286d" d="M6.6 10.8a15.1 15.1 0 0 0 6.6 6.6l2.2-2.2a1 1 0 0 1 1-.25 11.4 11.4 0 0 0 3.6.57 1 1 0 0 1 1 1V20a1 1 0 0 1-1 1A17 17 0 0 1 3 4a1 1 0 0 1 1-1h3.5a1 1 0 0 1 1 1c0 1.250.2 2.45.57 3.57a1 1 0 0 1-.25 1z"/></svg>
        <span>(555) 317-4860</span>
      </div>
      <div class="contact__row">
        <svg class="contact__icon" viewBox="0 0 24 24" aria-hidden="true"><rect x="2" y="5" width="20" height="14" fill="#06286d"/><path d="M2 5l10 8 10-8" fill="none" stroke="#fff" stroke-width="1.6"/></svg>
        <span>marcus@bralvintrust.example</span>
      </div>
      <div class="contact__row">
        <svg class="contact__icon" viewBox="0 0 24 24" aria-hidden="true"><circle cx="12" cy="12" r="10" fill="#06286d"/><path d="M2 12h20M12 2c3 3 3 17 0 20M12 2c-3 3-3 17 0 20" fill="none" stroke="#fff" stroke-width="1.2"/></svg>
        <span>vendrikworks.example</span>
      </div>
      <div class="contact__address">18716 52nd Avenue S, Marlow Falls,<br>OR 98417</div>
    </div>
  </section>

  <section class="card card--back" aria-label="Business card back">
    <div class="back-brand">
      <div class="back-brand__name">Vendrik Works</div>
      <div class="back-brand__rule"></div>
    </div>
  </section>
</main>
</body>
</html>
```